Buch-/E-Book-Cover für Autobiografie
Zielgruppe
Ich bin Autor und habe soeben meine Autobiografie verfasst. Sie handelt hauptsächlich von meiner Flagfootball Karriere und meinem Weg vom American Football Fan zum Flagfootball Weltmeister.
Ich benötige ein Design für das Cover des Buches im DIN A5 Format. Es sollte sehr edel aussehen.
Buchtitel: Nachtfalke
Untertitel: Mein Weg vom ersten Wurf zum Weltmeistertitel im Flagfootball
Aufgabenstellung
Auf der Vorderseite sollte eines der mitgeschickten Bilder, der Titel, der Untertitel des Buches und mein Name stehen. Egal, welches Foto für die Vorderseite ausgewählt wird, der Football sollte jedenfalls gut erkennbar sein.
Auf der Rückseite eine Buchbeschreibung und drei kurze Statements von Testimonials.
Auf dem Buchrücken mein Name und der Buchtitel (ohne Untertitel).
Farblich sollte sich das Design an den Farben meiner Website anlehnen (Hauptfarben Gold, Weiss, Schwarz)

```html
<!DOCTYPE html>
<html lang="de">
<head>
<meta charset="utf-8">
<title>Nachtfalke – Buchumschlag</title>
<link href="https://fonts.googleapis.com/css2?family=Oswald:wght@300;400;600;700&family=Jost:wght@400&display=swap" rel="stylesheet">
<style>
  :root {
    --gold: #e5bc55;
    --black: #0c0c0c;
    --white: #ffffff;
    --shadow: #3a3428;
    --photo-light: #ebe8e2;
    --photo-mid: #d8d3c9;
  }
  * { margin: 0; padding: 0; box-sizing: border-box; }
  html, body { width: 1200px; height: 810px; overflow: hidden; background: var(--white); }
  .cover { position: relative; width: 1200px; height: 810px; display: flex; }

  /* Rückseite */
  .back { position: relative; width: 570px; height: 810px; background: var(--gold); }
  .back-title {
    position: absolute; left: 50px; top: 40px;
    font: 700 88px/1 "Oswald", sans-serif; color: var(--black); letter-spacing: 1px;
  }
  .back-subtitle {
    position: absolute; left: 50px; top: 152px;
    font: 400 30px/1.1 "Oswald", sans-serif; color: var(--white); text-transform: uppercase;
  }
  .back-photo {
    position: absolute; left: 49px; top: 243px; width: 213px; height: 284px;
    background: linear-gradient(160deg, #6f7a4a 0%, #3f4a2c 55%, #2a2a26 100%);
  }
  .back-motto {
    position: absolute; left: 58px; top: 540px;
    font: italic 600 30px/1 "Oswald", sans-serif; color: var(--white);
  }
  .back-blurb {
    position: absolute; left: 285px; top: 241px; width: 240px;
    font: 400 12.6px/18px "Jost", sans-serif; color: var(--black);
  }
  .back-blurb p + p { margin-top: 18px; }

  /* Buchrücken */
  .spine { position: relative; width: 59px; height: 810px; background: var(--black); }
  .spine-title, .spine-author {
    position: absolute; left: 50%; white-space: nowrap;
    transform: translate(-50%, -50%) rotate(-90deg);
  }
  .spine-title { top: 318px; font: 700 34px/1 "Oswald", sans-serif; color: var(--gold); }
  .spine-author { top: 555px; font: 300 22px/1 "Oswald", sans-serif; color: var(--white); letter-spacing: 7px; }

  /* Vorderseite */
  .front { position: relative; width: 571px; height: 810px; overflow: hidden; }
  .front-photo {
    position: absolute; inset: 0;
    background: linear-gradient(100deg, var(--photo-light) 0%, var(--photo-mid) 100%);
  }
  .front-author {
    position: absolute; left: 30px; top: 42px;
    font: 400 56px/1 "Oswald", sans-serif; color: var(--black);
  }
  .front-title {
    position: absolute; left: 28px; top: 112px;
    font: 700 104px/0.86 "Oswald", sans-serif; color: var(--gold);
    text-shadow: 3px 3px 0 var(--shadow);
  }
  .front-subtitle {
    position: absolute; left: 30px; top: 296px;
    font: 400 36px/1.12 "Oswald", sans-serif; color: var(--white); text-transform: uppercase;
  }
</style>
</head>
<body>
<div class="cover">
  <section class="back">
    <h2 class="back-title">NACHTFALKE</h2>
    <p class="back-subtitle">Mein Weg vom ersten Wurf<br>zum Flagfootball Weltmeistertitel</p>
    <div class="back-photo" role="img" aria-label="Foto des Autors im schwarzen T-Shirt mit Football vor grüner Hecke"></div>
    <p class="back-motto">“GO FOR GOLD”</p>
    <div class="back-blurb">
      <p>In meiner Autobiografie erzähle ich die spannende und einzigartige Geschichte, wie ich vom American Football Fan zum Flagfootball Weltmeister wurde. Motiviert durch das Verfolgen der Profiliga und einem zufälligen Treffen mit meinem großen Sportidol, wuchs in mir der Wunsch, selbst am Spielfeld zu stehen und Erfolge zu feiern. Doch wo sollte ich anfangen? Am besten bei null, denn ich hatte nie zuvor Flagfootball gespielt.</p>
      <p>Auf unterhaltsame und lustige Weise tauche ich in den Beginn meiner Reise in den frühen 2000er Jahren ein. Das Ziel fest vor Augen, gründete ich den ersten steirischen Flagfootball Verein und startete meinen Weg der mich bis zur Weltmeisterschaft führte, wo ich als Quarterback mit der österreichischen Nationalmannschaft den Titel holte.</p>
      <p>Begleite mich durch meine Geschichte und erlebe mit mir Höhen und Tiefen, Erfolge und Rückschläge und meinen größten Triumph.</p>
    </div>
  </section>

  <section class="spine">
    <span class="spine-title">NACHTFALKE</span>
    <span class="spine-author">KONRAD WIEBKE</span>
  </section>

  <section class="front">
    <div class="front-photo" role="img" aria-label="Foto des Autors im schwarzen T-Shirt, einen Football in der Hand, vor heller Wand"></div>
    <p class="front-author">KONRAD WIEBKE</p>
    <h1 class="front-title">NACHT<br>FALKE</h1>
    <p class="front-subtitle">Mein Weg vom ersten<br>Wurf zum Flagfootball<br>Weltmeistertitel</p>
  </section>
</div>
</body>
</html>
```